Business IT Services Billboard to attract local small businesses

We are Brivolane, a premier Managed Service Provider (MSP) specializing in comprehensive IT services and VOIP phone solutions exclusively for businesses. Our goal is to create a dynamic and visually engaging billboard advertisement that not only highlights our cutting-edge IT solutions but also emphasizes our state-of-the-art VOIP phone services. This billboard should communicate our commitment to providing innovative, reliable, and holistic technology solutions.
Target Market(s)
small business
Industry/Entity Type
Information Technology
Colors
Designer to choose colors to be used in the design.
Look and feel
Each slider illustrates characteristics of the customer's brand and the style your logo design should communicate.

```html
<!DOCTYPE html>
<html lang="en">
<head>
<meta charset="UTF-8">
<title>Brivolane Billboard</title>
<link href="https://fonts.googleapis.com/css2?family=Krona+One&family=Montserrat:wght@500;700&display=swap" rel="stylesheet">
<style>
  :root {
    --page-bg: #e9eef4;
    --navy-deep: #050d2a;
    --navy-mid: #0b2a6e;
    --fiber-blue: #1f5fc4;
    --band-blue: #2aa7e4;
    --band-light: #6fd0f7;
    --photo-light: #4f8fe0;
    --photo-dark: #163f9a;
    --white: #ffffff;
  }
  * { margin: 0; padding: 0; box-sizing: border-box; }
  html, body { width: 1200px; height: 840px; overflow: hidden; }
  body { background: var(--page-bg); position: relative; font-family: "Montserrat", sans-serif; }

  .billboard {
    position: absolute; left: 40px; top: 235px;
    width: 1120px; height: 370px; overflow: hidden;
    background: var(--navy-deep);
  }
  .billboard__backdrop {
    position: absolute; inset: 0;
    background:
      radial-gradient(ellipse at 50% 55%, rgba(120,190,255,0.55) 0%, rgba(31,95,196,0.35) 30%, transparent 65%),
      linear-gradient(180deg, var(--navy-deep) 0%, var(--navy-mid) 45%, var(--fiber-blue) 50%, var(--navy-mid) 70%, var(--navy-deep) 100%);
  }
  .billboard__streak {
    position: absolute; left: 0; top: 168px; width: 890px; height: 6px;
    background: linear-gradient(90deg, transparent, rgba(200,235,255,0.9) 40%, rgba(200,235,255,0.9) 70%, transparent);
  }
  .brand-name {
    position: absolute; left: 40px; top: 22px; width: 1040px;
    font-family: "Krona One", sans-serif; font-size: 92px; line-height: 1;
    color: var(--white); letter-spacing: 2px; text-align: center;
  }
  .headline {
    position: absolute; left: 45px; top: 132px; width: 1040px;
    font-weight: 700; font-size: 28px; color: var(--white); text-align: center;
  }
  .offer-band {
    position: absolute; left: 0; top: 186px; width: 890px; height: 72px;
    background: linear-gradient(90deg, var(--band-blue), var(--band-light) 60%, var(--band-blue));
    display: flex; flex-direction: column; justify-content: center; align-items: center;
  }
  .offer-band__line {
    font-family: "Krona One", sans-serif; font-size: 23px; line-height: 1.3;
    color: var(--white);
  }
  .product-photo {
    position: absolute; left: 890px; top: 172px; width: 230px; height: 198px;
    background: radial-gradient(ellipse at 60% 60%, var(--photo-light), var(--photo-dark) 80%);
  }
  .call-to-action {
    position: absolute; left: 35px; top: 322px;
    font-weight: 500; font-size: 17px; letter-spacing: 2.5px; color: var(--white);
  }
  .web-address {
    position: absolute; left: 415px; top: 295px;
    font-weight: 700; font-size: 40px; color: var(--white);
  }
</style>
</head>
<body>
  <section class="billboard">
    <div class="billboard__backdrop" role="img" aria-label="Glowing blue fiber optic strands over a server rack"></div>
    <div class="billboard__streak"></div>
    <h1 class="brand-name">BRIVOLANE</h1>
    <p class="headline">Elevate Your Business with Next-Gen IT and VOIP Services</p>
    <div class="offer-band">
      <span class="offer-band__line">Innovative IT and VOIP Solutions</span>
      <span class="offer-band__line">Tailored for Your Business Success.</span>
    </div>
    <div class="product-photo" role="img" aria-label="Office VOIP desk phone in blue light"></div>
    <p class="call-to-action">TRANSFORM YOUR TECH TODAY</p>
    <p class="web-address">www.brivolane.com</p>
  </section>
</body>
</html>
```